Ridgefold MMA - Ridgefold Way - 7-5-4

This will be for a wall logo. Probably printed on vinyl to adhere to the wall. This a rough draft concept of the project, but we're certainly open to other designs. Red, Black and White are the main colors we would like to use. The triangle motif is important, it denotes stability and base, which are important in jiu jistu.
The Ridgefold Way (7-5-4)
7 Virtues of a Warrior (Bushido)
R Rectitude
Doing what is right w/o regard for the consequences
C Courage
Inner strength to resist opposition. Courage not just to step on the mat but to make the right decisions
B Benevolence
Mindset to do good. Be kind and generous
P Politeness
Proper consideration and courtesy to others
L Loyalty
Faithfulness & Alliance. Not blind allegiance
H Honesty / Sincerity
Be a man of your word. Do what you say you will
Genuine Integrity in character & action
H Honor
Profound respect & ethical conduct
Make the right decisions to be worthy of respectability
5 Keys to Health
Nutrition - Eat sensibly
Exercise - Stay fit and ready
Rest - Recovery and Recharge
Hygiene - Stay Clean
Attitude - Assume positive intent
Look at life in a positive way
4 States of Mind (Spirit of Budo)
Shoshin - Beginners Mind
Be open to new ideas
Eager to Learn
Zanshin – Remaining Mind
Being Alert and Aware, but relaxed
Be Prepared
Mushin – No Mind (Clear Mind)
Be able to act in the moment without having to think
Fudoshin – Immovable Mind
Emotional Balance
Free from anger, fear, & doubt

```html
<!DOCTYPE html>
<html lang="en">
<head>
<meta charset="utf-8">
<title>The Ridgefold Way 7-5-4</title>
<link rel="stylesheet" href="https://fonts.googleapis.com/css2?family=Permanent+Marker&family=Saira+Semi+Condensed:wght@500;600;700&display=swap">
<style>
  :root {
    --red-deep: #b5121b;
    --red-mid: #d41920;
    --red-bright: #e3242b;
    --sun: #ee4c3e;
    --ink: #0d0b0b;
    --white: #ffffff;
    --rule: rgba(0,0,0,0.55);
    --rule-light: rgba(212,25,32,0.9);
  }
  * { box-sizing: border-box; margin: 0; padding: 0; }
  html, body { width: 848px; height: 1200px; overflow: hidden; background: var(--red-deep); }
  .poster {
    position: relative; width: 848px; height: 1200px; overflow: hidden;
    font-family: "Saira Semi Condensed", "Arial Narrow", sans-serif;
    color: var(--white);
  }
  .backdrop { position: absolute; inset: 0; }
  .block { position: absolute; text-align: center; }
  .numeral {
    font-family: "Permanent Marker", cursive;
    font-size: 50px; line-height: 1;
  }
  .column-title { font-size: 28px; font-weight: 600; line-height: 1.1; }
  .column-sub { font-size: 20px; font-weight: 600; line-height: 1.1; }
  .list-item { padding: 7px 0; border-bottom: 1px solid var(--rule); }
  .list-item:last-child { border-bottom: none; }
  .item-name { font-size: 16px; font-weight: 600; line-height: 1.15; }
  .item-text { font-size: 15px; font-weight: 500; line-height: 1.3; }
  .health { left: 50px; top: 290px; width: 170px; }
  .health .list-item { padding: 6px 0 8px; }
  .virtues-head { left: 264px; top: 292px; width: 320px; }
  .virtues-head .column-title { font-size: 33px; font-weight: 700; line-height: 1.22; }
  .mind { left: 585px; top: 294px; width: 246px; }
  .mind .list-item { padding: 8px 0 9px; border-bottom-color: var(--rule); }
  .virtue .virtue-name { font-size: 28px; font-weight: 600; line-height: 1.1; }
  .virtue .initial {
    font-family: "Permanent Marker", cursive; color: var(--red-bright);
    font-size: 34px; margin-right: 3px;
  }
  .virtue .virtue-text { font-size: 15px; font-weight: 500; line-height: 1.35; margin-top: 6px; }
  .rectitude { left: 324px; top: 620px; width: 200px; }
  .courage { left: 294px; top: 760px; width: 260px; }
  .benevolence { left: 226px; top: 910px; width: 190px; }
  .politeness { left: 430px; top: 916px; width: 190px; }
  .loyalty { left: 100px; top: 1040px; width: 180px; }
  .honesty { left: 294px; top: 1040px; width: 260px; }
  .honor { left: 564px; top: 1040px; width: 220px; }
  .honor .virtue-text, .honesty .virtue-text, .loyalty .virtue-text { margin-top: 2px; }
  .brand {
    position: absolute; left: 660px; top: 822px; width: 150px;
    display: flex; flex-direction: column; align-items: center; gap: 6px;
    font-size: 28px; font-weight: 700; line-height: 1; color: var(--white);
  }
  .brand-mark { width: 18px; height: 18px; background: var(--ink); }
</style>
</head>
<body>
<main class="poster">
  <svg class="backdrop" width="848" height="1200" viewBox="0 0 848 1200">
    <defs>
      <radialGradient id="glow" cx="50%" cy="37%" r="60%">
        <stop offset="0" stop-color="#e8262c"/>
        <stop offset="1" stop-color="#b5121b"/>
      </radialGradient>
      <linearGradient id="hills" x1="0" y1="0" x2="0" y2="1">
        <stop offset="0" stop-color="#d41920" stop-opacity="0"/>
        <stop offset="1" stop-color="#9e0f17"/>
      </linearGradient>
      <path id="title-arc" d="M 94 440 A 330 330 0 0 1 754 440"/>
    </defs>
    <rect width="848" height="1200" fill="var(--red-deep)"/>
    <circle cx="424" cy="440" r="424" fill="url(#glow)"/>
    <rect class="landscape" role="img" aria-label="Misty red mountain ranges" x="0" y="640" width="848" height="560" fill="url(#hills)"/>
    <circle class="sun" cx="424" cy="412" r="167" fill="var(--sun)"/>
    <rect class="warrior" role="img" aria-label="Silhouette of a samurai with straw hat and swords" x="100" y="730" width="105" height="260" fill="var(--ink)" opacity="0.85"/>
    <polygon class="pyramid-edge" points="424,460 14,1192 834,1192" fill="var(--red-mid)"/>
    <polygon class="pyramid" points="424,482 28,1184 820,1184" fill="var(--ink)"/>
    <g stroke="var(--rule-light)" stroke-width="1">
      <line x1="365" y1="742" x2="483" y2="742"/>
      <line x1="375" y1="890" x2="473" y2="890"/>
      <line x1="424" y1="922" x2="424" y2="1012"/>
      <line x1="282" y1="1050" x2="282" y2="1140"/>
      <line x1="560" y1="1050" x2="560" y2="1140"/>
    </g>
    <text font-family="Permanent Marker, cursive" font-size="68" fill="var(--white)" text-anchor="middle">
      <textPath href="#title-arc" startOffset="50%">THE RIDGEFOLD WAY</textPath>
    </text>
    <text x="424" y="212" font-family="Permanent Marker, cursive" font-size="66" fill="var(--white)" text-anchor="middle">• 7-5-4 •</text>
  </svg>

  <section class="block health">
    <div class="numeral">5</div>
    <h2 class="column-title">Keys to Health</h2>
    <div class="list">
      <div class="list-item"><div class="item-name">NUTRITION</div><div class="item-text">Eat sensibly</div></div>
      <div class="list-item"><div class="item-name">EXERCISE</div><div class="item-text">Stay fit and ready</div></div>
      <div class="list-item"><div class="item-name">REST</div><div class="item-text">Recovery and Recharge</div></div>
      <div class="list-item"><div class="item-name">HYGIENE</div><div class="item-text">Stay Clean</div></div>
      <div class="list-item"><div class="item-name">ATTITUDE</div><div class="item-text">Assume positive intent Look at life in a positive way</div></div>
    </div>
  </section>

  <section class="block virtues-head">
    <div class="numeral">7</div>
    <h1 class="column-title">VIRTUES OF A WARRIOR<br>(BUSHIDO)</h1>
  </section>

  <section class="block mind">
    <div class="numeral">4</div>
    <h2 class="column-title">States of Mind</h2>
    <div class="column-sub">(SPIRIT OF BUDO)</div>
    <div class="list">
      <div class="list-item"><div class="item-name">SHOSHIN - Beginners Mind</div><div class="item-text">Be open to new ideas<br>Eager to Learn</div></div>
      <div class="list-item"><div class="item-name">ZANSHIN – Remaining Mind</div><div class="item-text">Being Alert and Aware,<br>but relaxed Be Prepared</div></div>
      <div class="list-item"><div class="item-name">MUSHIN – No Mind (Clear Mind)</div><div class="item-text">Be able to act in the moment without having to think</div></div>
      <div class="list-item"><div class="item-name">FUDOSHIN – Immovable Mind</div><div class="item-text">Emotional Balance<br>Free from anger, fear, &amp; doubt</div></div>
    </div>
  </section>

  <article class="block virtue rectitude"><div class="virtue-name"><span class="initial">R</span>Rectitude</div><p class="virtue-text">Doing what is right<br>w/o regard for<br>the consequences</p></article>
  <article class="block virtue courage"><div class="virtue-name"><span class="initial">C</span>Courage</div><p class="virtue-text">Inner strength to resist opposition. Courage not just to step on the mat but to make the right decisions</p></article>
  <article class="block virtue benevolence"><div class="virtue-name"><span class="initial">B</span>Benevolence</div><p class="virtue-text">Mindset to do good.<br>Be kind<br>and generous</p></article>
  <article class="block virtue politeness"><div class="virtue-name"><span class="initial">P</span>Politeness</div><p class="virtue-text">Proper consideration and courtesy to others</p></article>
  <article class="block virtue loyalty"><div class="virtue-name"><span class="initial">L</span>Loyalty</div><p class="virtue-text">Faithfulness &amp; Alliance.<br>Not blind allegiance</p></article>
  <article class="block virtue honesty"><div class="virtue-name"><span class="initial">H</span>Honesty / Sincerity</div><p class="virtue-text">Be a man of your word. Do what you say you will Genuine Integrity in character &amp; action</p></article>
  <article class="block virtue honor"><div class="virtue-name"><span class="initial">H</span>Honor</div><p class="virtue-text">Profound respect &amp; ethical conduct Make the right decisions to be worthy of respectability</p></article>

  <div class="brand"><span class="brand-name">Ridgefold MMA</span><span class="brand-mark"></span></div>
</main>
</body>
</html>
```